Create a Brochure Design for Brantley Homecare

Brantley Homecare is a subsidiary of the Brantley Care Group. This brochure is specifically for the Brantley Homecare company and brand. Create a 3 panel, A4, front and back, tri-fold brochure. This brochure will be a way to introduce our Homecare services to the community, prospective clients, and various referral partners. The brochure must be eye catching, unique in its deliverables and demonstrate both attention to detail and comfort. Our organization is sophisticated and built around warmth, care and individualized personal attention. The most important aspect of this design is to focus on creating a nurturing, warm, and inviting feel where you would want to have a Nurse or Nurse’s Aide in your own home or a loved one’s home.

I am open to the creativity of the designer to develop something based on the above criteria; however I would like the design to work well with the existing collateral material. What I mean by that is that while I want everything to have its own personality and stand out as its own brand representative, I still need to be able to tell that the overall design concept stays stylistically inside of the same ‘family’ of existing designed material. Because of this, below I would like for the designer to pull inspiration from the link to our website (Located below) as well as from the attachment of our recently refreshed business cards (Attached). This should allow each design to be unique and creative, while still staying inside of a framework and the feel/style that I am looking for.

Finally, I want all the designers to understand that this brochure design is for a private, in home, healthcare company where we are responsible for providing personalized care for a culturally and ethnically diverse make-up clientele of all ages. The photos that are used must represent an image of warmth, care, and a positive interaction between client and caregiver.

Look under the Brantley Homecare tab at www.brantleycaregroup-example.net

Industry/Entity Type

Healthcare

Requirements
Must have
• • The Brantley Homecare company logo must be included.

```html
<!DOCTYPE html>
<html lang="en">
<head>
<meta charset="utf-8">
<title>Brantley Homecare – Brochure Panel</title>
<link rel="stylesheet" href="https://fonts.googleapis.com/css2?family=EB+Garamond:ital,wght@0,400;0,600;1,400;1,600&display=swap">
<style>
  :root {
    --peach: #fdd79f;
    --peach-light: #fee5bd;
    --pink: #ef88b3;
    --ink: #1d1a17;
    --photo-warm-a: #e6d6c8;
    --photo-warm-b: #b89a86;
    --photo-face-a: #a8735a;
    --photo-face-b: #4b3128;
    --photo-room-a: #b9c9a0;
    --photo-room-b: #7d7468;
  }
  * { margin: 0; padding: 0; box-sizing: border-box; }
  html, body { width: 1200px; height: 933px; overflow: hidden; background: var(--peach); }
  .panel {
    position: relative;
    width: 1200px;
    height: 933px;
    background: var(--peach);
    font-family: "EB Garamond", Garamond, serif;
    color: var(--ink);
    overflow: hidden;
  }
  .photo { position: absolute; top: 14px; height: 270px; }
  .photo--companions { left: 0; width: 410px; background: linear-gradient(135deg, var(--photo-warm-a), var(--photo-warm-b)); }
  .photo--caregiver { left: 412px; width: 392px; background: radial-gradient(ellipse at 50% 45%, var(--photo-face-a), var(--photo-face-b)); }
  .photo--activity { left: 806px; width: 394px; background: linear-gradient(110deg, var(--photo-room-b), var(--photo-room-a) 60%, #d8c08a); }
  .shapes { position: absolute; inset: 0; width: 1200px; height: 933px; }
  .column {
    position: absolute;
    top: 322px;
    width: 350px;
    font-size: 22.5px;
    line-height: 40px;
  }
  .column--intro { left: 20px; }
  .column--promise { left: 425px; }
  .column--supervision { left: 829px; }
  .column p { margin: 0; }
  .gap { height: 40px; }
  .emph { font-weight: 600; font-style: italic; }
  .duty { font-style: italic; }
  .contact {
    position: absolute;
    left: 20px;
    top: 850px;
    font-family: Arial, Helvetica, sans-serif;
    font-size: 16.5px;
    line-height: 23px;
    color: #111;
  }
  .contact .web { font-size: 18px; }
  .brand {
    position: absolute;
    left: 990px;
    top: 832px;
    width: 190px;
    text-align: center;
  }
  .brand__name {
    font-size: 24px;
    line-height: 28px;
    color: var(--ink);
    font-weight: 400;
  }
</style>
</head>
<body>
<main class="panel">
  <div class="photo photo--companions" role="img" aria-label="Photo: smiling senior woman with two caregivers"></div>
  <div class="photo photo--caregiver" role="img" aria-label="Photo: close-up portrait of a smiling caregiver"></div>
  <div class="photo photo--activity" role="img" aria-label="Photo: senior woman and caregiver playing a game together"></div>

  <svg class="shapes" viewBox="0 0 1200 933" aria-hidden="true">
    <path fill="var(--pink)" d="M0,0 H1200 V8 C900,-4 600,34 300,20 C180,14 80,10 0,16 Z"/>
    <path fill="var(--pink)" d="M0,222 C250,268 600,292 900,286 C1020,283 1120,274 1200,268 V312 C1000,300 700,306 400,302 C220,298 100,280 0,266 Z"/>
    <path fill="var(--peach)" d="M0,266 C100,280 220,298 400,302 C700,306 1000,300 1200,312 V933 H0 Z"/>
    <path fill="var(--peach-light)" d="M0,745 C300,720 600,770 900,760 C1030,756 1130,740 1200,728 V933 H0 Z" opacity="0.8"/>
    <path fill="var(--peach)" d="M0,815 C250,780 520,840 820,820 C990,808 1120,790 1200,780 V933 H0 Z" opacity="0.6"/>
  </svg>

  <section class="column column--intro">
    <p>We provide in-home services ranging from <span class="emph">light housekeeping to personal care and skilled nursing</span>. We strive to give compassionate, dependable care of the highest quality while maintaining extremely competitive rates. Everything we do is geared toward meeting the individual needs of our clients.</p>
  </section>

  <section class="column column--promise">
    <p><span class="emph">Whether you need a little help or a lot of help, you’ll find that Brantley Homecare’s services</span> are a cut above the rest. The Brantley Way is special; it is compassionate, professional, dependable, and flexible.</p>
    <p>All of our Care Professionals:</p>
    <p>Are bonded, insured, and supervised;</p>
    <p>Have passed both criminal and abuse background checks;</p>
  </section>

  <section class="column column--supervision">
    <p>Have been screened for TB;</p>
    <p>Are certified in CPR and First Aid</p>
    <div class="gap"></div>
    <p><span class="emph">All client care is supervised by a licensed Nurse Care Consultant</span> whose duties include:</p>
    <p class="duty">Regular home visits</p>
    <p class="duty">Client evaluation</p>
    <p class="duty">Care Professional supervision</p>
    <p class="duty">Revising/updating client care plans</p>
    <p class="duty">24/7 phone support</p>
  </section>

  <div class="contact">
    <p>For further information:</p>
    <p class="web">www.brantleyhomecare-example.net</p>
  </div>

  <div class="brand">
    <p class="brand__name">Brantley Homecare</p>
  </div>
</main>
</body>
</html>
```